Ferris Contracting LLC Business Card Design

I am looking for a creative and unique business card design. We are a commercial construction general contractor. With the name "FERRIS" Contracting, I am hoping to see some neat designs that correlate with the name.

```html
<!DOCTYPE html>
<html lang="en">
<head>
<meta charset="utf-8">
<title>Ferris Contracting LLC – Business Card</title>
<link rel="stylesheet" href="https://fonts.googleapis.com/css2?family=Montserrat:wght@400;500;700&display=swap">
<style>
  :root {
    --page-bg: #d9d6d1;
    --card-top: #f4f5f6;
    --card-bottom: #e4e7ea;
    --card-edge: #ffffff;
    --brand-blue: #1a73a8;
    --brand-blue-light: #2a8fd0;
    --steel-grey: #8d8a86;
    --ink: #1d1f22;
  }
  * { box-sizing: border-box; margin: 0; padding: 0; }
  html, body {
    width: 1200px;
    height: 969px;
    overflow: hidden;
  }
  body {
    background: var(--page-bg);
    font-family: "Montserrat", sans-serif;
    color: var(--ink);
    position: relative;
  }
  .business-card {
    position: absolute;
    left: 80px;
    top: 188px;
    width: 1040px;
    height: 592px;
    border-radius: 26px;
    background: linear-gradient(160deg, var(--card-top), var(--card-bottom));
    border: 1.5px solid var(--card-edge);
    box-shadow: 0 14px 40px rgba(0,0,0,0.18);
    overflow: hidden;
  }
  .holder-name {
    position: absolute;
    left: 53px;
    top: 98px;
    font-size: 36px;
    font-weight: 700;
    letter-spacing: 0.2px;
    color: var(--brand-blue);
    line-height: 1;
  }
  .holder-title {
    position: absolute;
    left: 53px;
    top: 148px;
    font-size: 22px;
    font-weight: 500;
    line-height: 1;
  }
  .office-address {
    position: absolute;
    left: 53px;
    top: 222px;
    font-size: 22px;
    font-weight: 500;
    line-height: 37px;
    font-style: normal;
  }
  .contact-list {
    position: absolute;
    left: 53px;
    top: 338px;
    list-style: none;
  }
  .contact-item {
    display: flex;
    align-items: center;
    height: 37px;
    font-size: 22px;
    font-weight: 500;
  }
  .contact-icon {
    width: 21px;
    height: 21px;
    margin-right: 18px;
    flex: none;
  }
  .company-line {
    position: absolute;
    left: 53px;
    top: 460px;
    font-size: 22px;
    font-weight: 500;
    letter-spacing: 0.6px;
  }
  .brand-lockup {
    position: absolute;
    left: 520px;
    top: 190px;
    width: 470px;
    display: flex;
    align-items: center;
    gap: 22px;
  }
  .brand-dot {
    width: 74px;
    height: 74px;
    border-radius: 50%;
    background: var(--brand-blue);
    flex: none;
  }
  .brand-name {
    font-size: 44px;
    font-weight: 700;
    line-height: 1.1;
    color: var(--brand-blue);
    letter-spacing: 1px;
  }
  .accent-band {
    position: absolute;
    left: 0;
    bottom: 0;
    width: 1040px;
    height: 40px;
  }
</style>
</head>
<body>
  <section class="business-card" aria-label="Ferris Contracting LLC business card">
    <h1 class="holder-name">DANA WHITFIELD</h1>
    <p class="holder-title">Managing director</p>

    <address class="office-address">
      2740 Harlow Ave, Ste<br>
      210, Carver, TX 75044
    </address>

    <ul class="contact-list">
      <li class="contact-item">
        <svg class="contact-icon" viewBox="0 0 24 24" aria-hidden="true">
          <path fill="var(--brand-blue)" d="M2 8c0-2 3-4 10-4s10 2 10 4v2h-5V8H7v2H2zM6 11h12l3 8H3z"/>
          <circle cx="12" cy="15" r="2.4" fill="#fff"/>
        </svg>
        555-014-2871
      </li>
      <li class="contact-item">
        <svg class="contact-icon" viewBox="0 0 24 24" aria-hidden="true">
          <rect x="2" y="6" width="20" height="13" rx="1" fill="var(--brand-blue)"/>
          <path d="M2.5 6.5 12 13.5 21.5 6.5" fill="none" stroke="#fff" stroke-width="1.6"/>
        </svg>
        hello@ferrisbuild.com
      </li>
      <li class="contact-item">
        <svg class="contact-icon" viewBox="0 0 24 24" aria-hidden="true">
          <circle cx="12" cy="12" r="10" fill="var(--brand-blue)"/>
          <path d="M2 12h20M12 2c-3.5 3-3.5 17 0 20M12 2c3.5 3 3.5 17 0 20" fill="none" stroke="#fff" stroke-width="1.3"/>
        </svg>
        www.ferrisbuild.com
      </li>
    </ul>

    <p class="company-line">"FERRIS" Contracting</p>

    <div class="brand-lockup">
      <span class="brand-dot" aria-hidden="true"></span>
      <span class="brand-name">FERRIS<br>CONTRACTING</span>
    </div>

    <svg class="accent-band" viewBox="0 0 1040 40" preserveAspectRatio="none" aria-hidden="true">
      <defs>
        <linearGradient id="band-blue" x1="0" x2="1" y1="0" y2="0">
          <stop offset="0" stop-color="var(--brand-blue)"/>
          <stop offset="0.5" stop-color="var(--brand-blue-light)"/>
          <stop offset="1" stop-color="var(--brand-blue)"/>
        </linearGradient>
      </defs>
      <polygon points="0,0 569,0 546,40 0,40" fill="url(#band-blue)"/>
      <polygon points="569,0 818,0 796,40 546,40" fill="var(--steel-grey)" opacity="0.75"/>
      <polygon points="828,0 1040,0 1040,40 806,40" fill="url(#band-blue)"/>
    </svg>
  </section>
</body>
</html>
```